Brell Harbor Company Business Cards

Front and Back Business Card - logo and text setup - cool design. I need workable photoshop or illustrator files so I can setup each employee card with design that is created
Updates

Hi everyone, thank you for the great entries. Please no more white and blue cards - there are so many already - black and silver only now please. thanks!

Target Market(s)

Construction Industry - Facility Managers

Industry/Entity Type

Construction

Contact Information for Business Card

I really like contemporary simplistic looks - clean neat....not opposed to seeing some black backrounds

Requirements
Must have
• Logo/website address with design on front only - www.brellharbor-example.com (logo attached)
• Back:
• Name/Title/Company Address/Phone/email address
Nice to have
• Cool design
Should not have
• Nothing gimmicky like Fire or Water - since we are a Fire Protection company - it has all been done

```html
<!DOCTYPE html>
<html lang="en">
<head>
<meta charset="utf-8">
<title>Brell Harbor Company – Business Cards</title>
<link href="https://fonts.googleapis.com/css2?family=Libre+Baskerville:wght@700&family=Outfit:wght@500;600;800&display=swap" rel="stylesheet">
<style>
  :root {
    --page: #ffffff;
    --wine: #8b1838;
    --navy: #23407a;
    --white: #ffffff;
    --peach-light: #fbd8cc;
    --peach: #f6a07f;
    --coral: #ee4e35;
  }
  * { box-sizing: border-box; margin: 0; padding: 0; }
  html, body { width: 1000px; height: 1200px; overflow: hidden; background: var(--page); }
  .canvas { position: relative; width: 1000px; height: 1200px; font-family: "Outfit", sans-serif; }
  .card { position: absolute; background: var(--wine); overflow: hidden; }
  .card--front { left: 165px; top: 125px; width: 663px; height: 428px; }
  .card--back { left: 162px; top: 644px; width: 663px; height: 429px; }
  .abs { position: absolute; }

  .holder-name { left: 47px; top: 48px; font-family: "Libre Baskerville", serif; font-weight: 700; font-size: 42px; color: var(--white); }
  .holder-title { left: 47px; top: 134px; font-weight: 800; font-size: 23px; color: var(--navy); }

  .contact-list { left: 362px; top: 170px; list-style: none; }
  .contact-list li { display: flex; align-items: center; height: 34px; color: var(--white); font-weight: 600; font-size: 16.5px; }
  .contact-list li:last-child { font-size: 18px; }
  .contact-list svg { width: 22px; height: 22px; margin-right: 10px; flex: none; }

  .pattern-strip { left: 7px; top: 353px; width: 650px; height: 67px; background: var(--white); }

  .brand-band { left: 3px; top: 162px; width: 657px; height: 102px; background: var(--white); display: flex; align-items: center; justify-content: center; gap: 12px; }
  .brand-mark { width: 18px; height: 18px; background: var(--coral); }
  .brand-name { font-weight: 800; font-size: 40px; color: var(--navy); letter-spacing: -0.5px; }

  .website { left: 0; width: 100%; top: 398px; display: flex; justify-content: center; align-items: center; gap: 9px; color: var(--white); font-weight: 600; font-size: 16px; transform: translateX(-24px); }
  .website svg { width: 19px; height: 19px; }
</style>
</head>
<body>
<div class="canvas">

  <section class="card card--front" aria-label="Business card front">
    <svg class="abs" style="left:0;top:0" width="663" height="428" role="img" aria-label="Rising staircase of small square dots in peach tones">
      <defs>
        <linearGradient id="stairTone" x1="0" y1="1" x2="1" y2="0">
          <stop offset="0" stop-color="#fbd8cc" stop-opacity="0.35"/>
          <stop offset="1" stop-color="#f6a07f" stop-opacity="0.45"/>
        </linearGradient>
      </defs>
      <polygon points="30,330 42,330 420,55 420,0 405,0 30,255" fill="url(#stairTone)"/>
    </svg>

    <h1 class="abs holder-name">Name:</h1>
    <p class="abs holder-title">Title:</p>

    <ul class="abs contact-list">
      <li>
        <svg viewBox="0 0 24 24" fill="none" stroke="#23407a" stroke-width="2"><rect x="7" y="2" width="10" height="20" rx="2"/><line x1="10" y1="18" x2="14" y2="18"/></svg>
        +00000 000 00
      </li>
      <li>
        <svg viewBox="0 0 24 24" fill="#23407a"><path d="M6.6 10.8a15 15 0 0 0 6.6 6.6l2.2-2.2a1 1 0 0 1 1-.25 11.4 11.4 0 0 0 3.6.57 1 1 0 0 1 1 1V20a1 1 0 0 1-1 1A17 17 0 0 1 3 4a1 1 0 0 1 1-1h3.5a1 1 0 0 1 1 1c0 1.25.2 2.45.57 3.57a1 1 0 0 1-.25 1z"/></svg>
        +39 000 55 01 234
      </li>
      <li>
        <svg viewBox="0 0 24 24" fill="none" stroke="#23407a" stroke-width="1.8"><rect x="2" y="5" width="20" height="14"/><polyline points="2,5 12,13 22,5"/></svg>
        example@example.com
      </li>
      <li>
        <svg viewBox="0 0 24 24" fill="#23407a"><path d="M12 2a7 7 0 0 0-7 7c0 5 7 13 7 13s7-8 7-13a7 7 0 0 0-7-7zm0 9.5a2.5 2.5 0 1 1 0-5 2.5 2.5 0 0 1 0 5z"/></svg>
        Address:
      </li>
    </ul>

    <svg class="abs pattern-strip" width="650" height="67" role="img" aria-label="Grid of small square dots fading from pale peach to coral">
      <defs>
        <linearGradient id="stripTone" x1="0" y1="0" x2="1" y2="0">
          <stop offset="0" stop-color="#fbd8cc" stop-opacity="0.45"/>
          <stop offset="1" stop-color="#ee4e35" stop-opacity="0.55"/>
        </linearGradient>
      </defs>
      <rect x="24" y="6" width="606" height="55" fill="url(#stripTone)"/>
    </svg>
  </section>

  <section class="card card--back" aria-label="Business card back">
    <svg class="abs" style="left:28px;top:36px" width="608" height="92" role="img" aria-label="Rows of small square dots in coral and pale peach">
      <defs>
        <linearGradient id="dotsTone" x1="0" y1="0" x2="0" y2="1">
          <stop offset="0" stop-color="#ee4e35" stop-opacity="0.5"/>
          <stop offset="1" stop-color="#fbd8cc" stop-opacity="0.45"/>
        </linearGradient>
      </defs>
      <rect width="608" height="92" fill="url(#dotsTone)"/>
    </svg>

    <div class="abs brand-band">
      <span class="brand-mark" aria-hidden="true"></span>
      <span class="brand-name">Brell Harbor</span>
    </div>

    <svg class="abs" style="left:28px;top:302px" width="608" height="92" role="img" aria-label="Rows of small square dots in coral and pale peach">
      <rect width="608" height="92" fill="url(#dotsTone)"/>
    </svg>

    <p class="abs website">
      <svg viewBox="0 0 24 24" fill="none" stroke="#ffffff" stroke-width="1.6"><circle cx="12" cy="12" r="10"/><ellipse cx="12" cy="12" rx="4.5" ry="10"/><line x1="2" y1="12" x2="22" y2="12"/><path d="M4 7h16M4 17h16"/></svg>
      www.brellharbor-example.com
    </p>
  </section>

</div>
</body>
</html>
```